Job advert for Forged Here Collective

I would like a poster graphic that I can promote on social media to advertise a job vacancy we will be promoting our upcoming jobs, here is the text...

WE ARE ON THE…

LOOKOUT
(maybe insert graphic or icon that fits with the message here)

For A

OPERATIONS AND HR MANAGER

MEMBERSHIP ADVISOR (EAST MIDLANDS)

SOCIAL MEDIA CONTENT CREATOR

THE UK’s FASTEST GROWING NETWORK FOR MANUFACTURERS

OFFICES IN BIRMINGHAM AND LEEDS - WE ARE AN INCLUSIVE EMPLOYER (use the equality logo provided here)

Target Market(s)

people looking to find a new job

Industry/Entity Type

Manufacture

Font styles to use
Sans Serif

Colors
f04a50
f68e4e
e667a6

Requirements
Must have
• Clear simple and contemporary style
Nice to have
• a nice graphic or icon to convey the text message
Should not have
• use of dark depressing colours

```html
<!DOCTYPE html>
<html lang="en">
<head>
<meta charset="utf-8">
<title>Forged Here Collective – We're Hiring</title>
<link rel="stylesheet" href="https://fonts.googleapis.com/css2?family=Open+Sans:wght@600&family=Raleway:wght@800;900&family=Arimo:ital@0;1&display=swap">
<style>
  :root {
    --paper: #f1f1f1;
    --red: #f04a50;
    --orange: #f68e4e;
    --pink: #e667a6;
    --ink: #1d1d1d;
    --shadow: #c4c4c4;
    --green: #9ac43c;
    --cv-brown: #7a5a14;
    --note-yellow: #fcc12d;
    --megaphone-light: #ffffff;
    --megaphone-grey: #d2d2d2;
  }
  * { margin: 0; padding: 0; box-sizing: border-box; }
  html, body { width: 883px; height: 1200px; overflow: hidden; background: var(--paper); }
  .poster { position: relative; width: 883px; height: 1200px; background: var(--paper); }

  .hashtag {
    position: absolute; top: 60px; left: 0; width: 100%;
    text-align: center; font: 25px/1.2 "Arimo", sans-serif; color: var(--red);
  }
  .megaphone {
    position: absolute; left: 109px; top: 100px; width: 190px; height: 268px;
    background: radial-gradient(circle at 55% 40%, var(--megaphone-light) 0%, var(--megaphone-grey) 75%);
    border-radius: 40px;
  }
  .headline { font-weight: 900; }
  .headline-small {
    position: absolute; left: 300px; top: 222px;
    font: 800 130px/1 "Raleway", sans-serif; color: var(--ink);
  }
  .headline-big {
    position: absolute; left: 0; top: 378px; width: 883px; text-align: center;
    font: 900 158px/1 "Raleway", sans-serif; color: var(--red);
    letter-spacing: 2px;
    text-shadow: 7px 7px 0 var(--shadow);
  }

  .roles {
    position: absolute; top: 630px; left: 0; width: 100%;
    list-style: none; text-align: center;
    font: 600 23px/41.6px "Open Sans", sans-serif; color: var(--ink);
  }
  .inclusive {
    position: absolute; top: 888px; left: 0; width: 100%; text-align: center;
    font: 800 44px/1 "Raleway", sans-serif; color: var(--orange);
    text-shadow: 2px 2px 0 #d9d9d9;
  }
  .partner {
    position: absolute; top: 970px; height: 46px;
    display: flex; align-items: center; gap: 8px;
    font: 600 16px/1 "Open Sans", sans-serif;
  }
  .partner-dot { width: 46px; height: 46px; border-radius: 50%; flex: none; }
  .partner--north { left: 136px; color: var(--green); }
  .partner--north .partner-dot { background: var(--green); }
  .partner--central { left: 355px; color: var(--red); }
  .partner--central .partner-dot { background: var(--red); }
  .equality-badge {
    position: absolute; top: 970px; left: 590px; width: 148px; height: 46px; border-radius: 23px;
    background: linear-gradient(90deg, var(--orange), var(--pink));
  }
  .cv-label {
    position: absolute; top: 1066px; left: 0; width: 100%; text-align: center;
    font: italic 23px/1.2 "Arimo", sans-serif; color: var(--cv-brown); letter-spacing: 2px;
  }
  .cv-email {
    position: absolute; top: 1108px; left: 281px; width: 321px; height: 52px;
    background: var(--note-yellow); box-shadow: 0 6px 8px rgba(0,0,0,0.25);
    display: flex; align-items: center; justify-content: center;
    font: 22px "Arimo", sans-serif; color: var(--ink);
  }
</style>
</head>
<body>
  <main class="poster">
    <p class="hashtag">#lookout</p>
    <div class="megaphone" role="img" aria-label="Megaphone illustration with sound lines"></div>
    <h1 class="headline">
      <span class="headline-small">we're</span>
      <span class="headline-big">HIRING!</span>
    </h1>

    <ul class="roles">
      <li>OPERATIONS AND HR MANAGER</li>
      <li>MEMBERSHIP ADVISOR (EAST MIDLANDS)</li>
      <li>SOCIAL MEDIA CONTENT CREATOR</li>
      <li>THE UK’s FASTEST GROWING NETWORK FOR MANUFACTURERS</li>
      <li>OFFICES IN BIRMINGHAM AND LEEDS</li>
    </ul>

    <h2 class="inclusive">WE ARE AN INCLUSIVE EMPLOYER</h2>

    <div class="partner partner--north"><span class="partner-dot"></span>Forged Here North</div>
    <div class="partner partner--central"><span class="partner-dot"></span>Forged Here Central</div>
    <div class="equality-badge" role="img" aria-label="Inclusivity commitment badge"></div>

    <p class="cv-label">Send your CV to</p>
    <p class="cv-email">careers@forgedhere.example</p>
  </main>
</body>
</html>
```